Velmora Education General Flyer Design

Updates
Reason: We are very close to making a selection but would like to provide a little more time for some of the designers to complete their revisions.
Target Market(s)
Secondary school students
Industry/Entity Type
Education
Requirements
Must have
- company logo and company name (see attached file)

```html
<!DOCTYPE html>
<html lang="en">
<head>
<meta charset="utf-8">
<title>Velmora Education – Math Tutoring Flyer</title>
<link href="https://fonts.googleapis.com/css2?family=Alfa+Slab+One&family=Merriweather:wght@700;900&family=Permanent+Marker&family=Roboto+Condensed:wght@400;700&display=swap" rel="stylesheet">
<style>
  :root{
    --yellow:#f7d51c;
    --yellow-light:#fbe66a;
    --red:#e3262b;
    --red-dark:#b5161b;
    --blue:#33a9e6;
    --blue-dark:#1d7fbf;
    --green-board:#23453a;
    --green-text:#3b8a2c;
    --ink:#2b2b2b;
    --white:#ffffff;
    --gold:#f5d23a;
  }
  *{margin:0;padding:0;box-sizing:border-box}
  html,body{width:798px;height:1200px;overflow:hidden;background:var(--yellow)}
  .flyer{position:relative;width:798px;height:1200px;overflow:hidden;background:var(--yellow);font-family:"Roboto Condensed",Arial,sans-serif;color:var(--ink)}
  .shapes{position:absolute;inset:0}
  .hero-photo{position:absolute;left:0;top:0;width:798px;height:420px;
    background:radial-gradient(ellipse at 40% 45%,#3d6656 0%,var(--green-board) 55%,#14281f 100%);
    clip-path:polygon(0 0,100% 0,100% 68%,0 100%)}
  .brand{position:absolute;left:560px;top:70px;width:210px;height:110px;background:var(--white);
    display:flex;align-items:center;justify-content:center;gap:10px;box-shadow:0 4px 10px rgba(0,0,0,.3)}
  .brand-square{width:18px;height:18px;background:var(--red)}
  .brand-name{font-family:"Merriweather",Georgia,serif;font-weight:900;font-size:30px;color:var(--red)}
  .trial{position:absolute;left:388px;top:338px;width:330px;height:58px;display:flex;align-items:center;justify-content:center;
    font-family:"Merriweather",Georgia,serif;font-weight:900;font-size:27px;color:var(--red-dark)}
  .tutor-box{position:absolute;left:22px;top:405px;width:318px;height:250px;background:var(--blue);
    border:3px solid var(--white);padding:16px 20px;box-shadow:0 4px 10px rgba(0,0,0,.25)}
  .tutor-title{font-family:"Merriweather",Georgia,serif;font-weight:900;font-size:27px;color:var(--gold);margin-bottom:12px}
  .tutor-list{list-style:none}
  .tutor-list li{display:flex;align-items:center;gap:10px;color:var(--white);font-size:20px;line-height:1.85}
  .tick{width:16px;height:16px;flex:none}
  .headline{position:absolute;left:360px;top:462px;width:420px;text-align:center}
  .headline-main{font-family:"Alfa Slab One",Georgia,serif;font-size:96px;line-height:1;color:var(--ink);letter-spacing:2px}
  .headline-sub{font-family:"Alfa Slab One",Georgia,serif;font-size:42px;line-height:1.15;color:var(--ink);margin-top:8px}
  .slogan{position:absolute;left:0;top:712px;width:798px;text-align:center;font-family:"Permanent Marker",cursive;
    color:var(--green-text);font-size:54px;line-height:1.15;letter-spacing:1px}
  .contact{position:absolute;left:56px;top:940px;list-style:none}
  .contact li{display:flex;align-items:flex-start;gap:14px;font-size:19px;color:var(--ink);margin-bottom:22px;line-height:1.3}
  .contact svg{width:20px;height:20px;flex:none;margin-top:2px}
  .call{position:absolute;left:470px;top:945px;width:290px;text-align:center;color:var(--red)}
  .call-title{font-weight:700;font-size:64px;line-height:1}
  .call-note{font-weight:700;font-size:27px;line-height:1.1}
  .call-phone{font-weight:700;font-size:50px;line-height:1.2}
</style>
</head>
<body>
<main class="flyer">
  <div class="hero-photo" role="img" aria-label="Photo of a frustrated student holding their head in front of a green chalkboard covered in math formulas"></div>

  <svg class="shapes" width="798" height="1200" viewBox="0 0 798 1200" aria-hidden="true">
    <!-- lower info panel -->
    <polygon points="0,900 798,830 798,1200 0,1200" fill="var(--yellow-light)"/>
    <!-- red accent bands -->
    <polygon points="0,880 798,808 798,830 0,902" fill="var(--red)"/>
    <polygon points="0,420 798,286 798,300 0,436" fill="var(--red)"/>
    <!-- trial banner -->
    <polygon points="388,338 730,338 712,396 388,396" fill="var(--white)"/>
    <polygon points="730,338 760,338 742,396 712,396" fill="var(--red)"/>
    <!-- brand ribbon -->
    <polygon points="548,60 780,60 780,190 548,190" fill="var(--red)"/>
  </svg>

  <div class="brand">
    <span class="brand-square"></span>
    <span class="brand-name">Velmora</span>
  </div>

  <div class="trial">Free Trial Lesson</div>

  <section class="tutor-box">
    <h2 class="tutor-title">Math We Tutor :</h2>
    <ul class="tutor-list">
      <li><svg class="tick" viewBox="0 0 16 16"><rect x="1" y="1" width="14" height="14" fill="none" stroke="#fff" stroke-width="1.5"/><path d="M4 8l3 3 5-6" fill="none" stroke="#fff" stroke-width="2"/></svg>Ontario Math G.9 – 12</li>
      <li><svg class="tick" viewBox="0 0 16 16"><rect x="1" y="1" width="14" height="14" fill="none" stroke="#fff" stroke-width="1.5"/><path d="M4 8l3 3 5-6" fill="none" stroke="#fff" stroke-width="2"/></svg>IB Math High Level , Standard</li>
      <li><svg class="tick" viewBox="0 0 16 16"><rect x="1" y="1" width="14" height="14" fill="none" stroke="#fff" stroke-width="1.5"/><path d="M4 8l3 3 5-6" fill="none" stroke="#fff" stroke-width="2"/></svg>Level, Math Studies</li>
      <li><svg class="tick" viewBox="0 0 16 16"><rect x="1" y="1" width="14" height="14" fill="none" stroke="#fff" stroke-width="1.5"/><path d="M4 8l3 3 5-6" fill="none" stroke="#fff" stroke-width="2"/></svg>AP Calculus AB/BC</li>
      <li><svg class="tick" viewBox="0 0 16 16"><rect x="1" y="1" width="14" height="14" fill="none" stroke="#fff" stroke-width="1.5"/><path d="M4 8l3 3 5-6" fill="none" stroke="#fff" stroke-width="2"/></svg>University Year 1 Calculus</li>
    </ul>
  </section>

  <div class="headline">
    <h1 class="headline-main">Math</h1>
    <p class="headline-sub">from Abstract<br>to Concrete</p>
  </div>

  <p class="slogan">WE CAN HELP MAKE<br>THE CONNECTION</p>

  <ul class="contact">
    <li><svg viewBox="0 0 20 20"><path d="M10 2L1 10h3v8h5v-5h2v5h5v-8h3z" fill="var(--red)"/></svg><span>4150 Alder Road, Unit 210<br>Northfield, ON L0R 2K5</span></li>
    <li><svg viewBox="0 0 20 20"><rect x="1" y="4" width="18" height="12" fill="var(--red)"/><path d="M1 4l9 7 9-7" fill="none" stroke="#fff" stroke-width="1.5"/></svg><span>Service@VelmoraEducation.com</span></li>
    <li><svg viewBox="0 0 20 20"><circle cx="10" cy="10" r="8" fill="var(--red)"/><path d="M2 10h16M10 2c3 3 3 13 0 16M10 2c-3 3-3 13 0 16" fill="none" stroke="#fff" stroke-width="1.2"/></svg><span>www.VelmoraEducation.com</span></li>
  </ul>

  <div class="call">
    <p class="call-title">Call Us</p>
    <p class="call-note">For More Information</p>
    <p class="call-phone">555-014-2387</p>
  </div>
</main>
</body>
</html>
```